Existing company needs Rebranding on logo and website!!

the company is called fund in Kenya (www.plorvexatrade.co.uk) check the site to see the existing site and logo, this has to change and must be completely different.

I want to the turn the website into a crowd funding site, but i want an inovative and interacive site. Have a look http://www.zentro.org/about/how or https://www.boldmuvi.com/ to get an idea of what is required. However i do not want my site to be anything like this. It is 2015 so web browser can do alot. when it comes to selecting project proposals on the site i want them them to pop up use your imagination your the desgner. ofcourse the site will be taking card payments and possibly bank transfers and maybe quidnest. the usual API are already on the site so you wont need to do much. the site is hosted by pagebloom so i do prefer it to stay there. i am familiar with that platform.

interms of creativity you have full control we wil be working closely and i expect to be kept in the loop as things develope.

the site will also need to be turn into a mobile app which serves different purposes depending if your an investor or project sponsor.

i will give you all the information required we can communicate on talvox email or telephone i am flexible.

many thanks

Target Market(s)

Investors

Industry/Entity Type

Finance

Number of Pages Required

5+ page

Font styles to use
Sans Serif

Colors
3176b5
f04a50
abd036
00a990

Requirements
Must have
• i want the designer to look at my existing site www.plorvexatrade.co.uk and come up with a better design concept.

```html
<!DOCTYPE html>
<html lang="en">
<head>
<meta charset="utf-8">
<title>fund in Kenya</title>
<link href="https://fonts.googleapis.com/css?family=Open+Sans:400,600,700|Roboto+Condensed:700&display=swap" rel="stylesheet">
<style>
:root{
  --teal:#00a990;
  --red:#f04a50;
  --blue:#3176b5;
  --lime:#abd036;
  --ink:#2f2f2f;
  --text:#5a5a5a;
  --muted:#8a8a8a;
  --line:#e3e3e3;
  --band:#f1f1f1;
  --dark:#262626;
  --darker:#1c1c1c;
}
*{box-sizing:border-box;margin:0;padding:0}
html,body{width:1200px;height:2340px;overflow:hidden;background:#fff}
body{font-family:"Open Sans",Arial,sans-serif;color:var(--text);font-size:14px;line-height:1.55;position:relative}
.heading{font-family:"Roboto Condensed","Arial Narrow",sans-serif;font-weight:700;text-transform:uppercase;color:var(--ink);letter-spacing:.3px}
.wrap{position:absolute;left:50px;width:1100px}

/* top bar */
.topbar{position:absolute;top:0;left:0;width:1200px;height:24px;background:var(--dark)}
.topbar .account{position:absolute;right:50px;top:0;display:flex;height:24px}
.topbar .account a{color:#fff;font-size:10px;font-weight:600;text-decoration:none;padding:0 12px;line-height:24px;background:var(--teal)}
.topbar .account a+a{background:#3b3b3b}

/* header */
.header{position:absolute;top:24px;left:0;width:1200px;height:56px;background:#fff}
.brand{position:absolute;left:50px;top:12px;display:flex;align-items:center;gap:10px}
.brand .dot{width:30px;height:30px;border-radius:50%;background:var(--red)}
.brand .name{font-family:"Open Sans",sans-serif;font-weight:700;font-size:20px;color:var(--ink);text-transform:uppercase;letter-spacing:.5px}
.nav{position:absolute;right:50px;top:0;display:flex;height:56px}
.nav a{font-size:10.5px;font-weight:600;color:var(--ink);text-decoration:none;padding:0 14px;line-height:56px;text-transform:uppercase}
.nav a.active{color:var(--teal);border-bottom:3px solid var(--teal)}

/* hero */
.hero{position:absolute;top:80px;left:0;width:1200px;height:460px;background:linear-gradient(180deg,#9dbbd6 0%,#c8d7e2 38%,#8a8f8e 62%,#5c6a4f 100%)}
.hero .caption{position:absolute;left:0;top:310px;width:1200px;height:44px;background:rgba(20,20,20,.55);text-align:center}
.hero .caption h1{font-family:"Roboto Condensed",sans-serif;font-weight:700;font-size:24px;color:#fff;text-transform:uppercase;line-height:44px;letter-spacing:.5px}
.hero .pager{position:absolute;top:384px;left:0;width:1200px;display:flex;justify-content:center;gap:8px}
.hero .pager span{width:9px;height:9px;border-radius:50%;background:rgba(255,255,255,.55)}
.hero .pager span.on{background:#fff}

/* featured */
.featured{top:580px;height:140px}
.featured .label{font-size:11px;font-weight:700;color:var(--ink);text-transform:uppercase}
.featured .logos{display:flex;justify-content:space-between;align-items:center;margin-top:40px;padding:0 20px}
.featured .badge{height:40px;background:#c9c9c9;border-radius:3px}

/* about / why */
.intro{top:770px;height:380px;display:flex;gap:40px}
.intro .col{flex:1;position:relative}
.intro h2{font-size:28px;margin-bottom:18px}
.intro p{font-size:13px;margin-bottom:12px}
.btn{display:inline-block;background:var(--teal);color:#fff;font-size:12px;font-weight:700;text-transform:uppercase;padding:10px 22px;text-decoration:none}
.intro .btn{position:absolute;left:0;bottom:24px}
.why-body{display:flex;gap:16px}
.why-media{width:250px;height:200px;flex:none;background:linear-gradient(135deg,#dfe6ea,#a9bccb 60%,#6d8aa2)}
.why-text h3{font-size:13px;font-weight:700;color:var(--teal);margin:6px 0 6px}
.why-text ul{list-style:none}
.why-text li{font-size:12.5px;padding-left:14px;position:relative;margin-bottom:6px}
.why-text li:before{content:"";position:absolute;left:0;top:7px;width:6px;height:6px;background:var(--teal)}

/* popular */
.popular-title{top:1180px;font-size:28px}
.popular{position:absolute;top:1236px;left:0;width:1200px;height:410px;background:var(--band)}
.cards{position:absolute;top:24px;left:50px;width:1100px;display:flex;gap:25px}
.card{flex:1;background:#fff;border:1px solid var(--line);padding:14px}
.card .media{height:150px}
.m-port{background:linear-gradient(180deg,#a7c4dd,#6d8fa9 55%,#b5483e)}
.m-road{background:linear-gradient(180deg,#c9dcec,#9aa3a6 55%,#5c6b3e)}
.m-pipe{background:linear-gradient(180deg,#c6d7e6,#d8b441 55%,#7b7f84)}
.card h4{font-size:14px;font-weight:700;color:var(--teal);margin:12px 0 6px}
.card p{font-size:12px;margin-bottom:12px}
.card .place{display:flex;align-items:center;gap:6px;font-size:11.5px;color:var(--muted)}
.card .bar{height:5px;background:var(--line);margin:10px 0 8px}
.card .bar span{display:block;height:5px;background:var(--teal);width:100%}
.card .stats{display:flex;gap:26px}
.card .stats b{display:block;font-size:12px;color:var(--ink)}
.card .stats small{font-size:10.5px;color:var(--muted)}

/* news */
.news-title{top:1676px;font-size:28px}
.news{top:1730px;display:grid;grid-template-columns:1fr 1fr;column-gap:50px;row-gap:36px}
.item{display:flex;gap:18px;height:140px}
.item .thumb{width:150px;height:120px;flex:none}
.t1{background:linear-gradient(135deg,#3a3a3a,#8c8c8c)}
.t2{background:linear-gradient(135deg,#6b7d8f,#c2a57e)}
.t3{background:linear-gradient(135deg,#524436,#b38c5c)}
.t4{background:linear-gradient(135deg,#6f8a3a,#d6c14e)}
.item h5{font-size:14px;font-weight:600;color:var(--red);margin-bottom:6px}
.item time{display:block;font-size:11px;color:var(--muted);margin-bottom:6px}
.item p{font-size:12.5px}

/* footer */
.footer{position:absolute;top:2192px;left:0;width:1200px;height:148px;background:var(--dark)}
.footer .links{position:absolute;left:50px;top:40px;display:flex;gap:28px}
.footer .links a{color:#fff;font-size:11px;font-weight:600;text-decoration:none;text-transform:uppercase}
.footer .social{position:absolute;right:50px;top:34px;display:flex;gap:6px}
.footer .social span{width:24px;height:24px;background:var(--blue)}
.footer .social span:nth-child(3){background:var(--red)}
.footer .social span:nth-child(4){background:var(--teal)}
.footer .base{position:absolute;left:0;top:98px;width:1200px;height:50px;background:var(--darker)}
.footer .base p{margin-left:50px;line-height:50px;font-size:10.5px;color:#9a9a9a}
</style>
</head>
<body>

<div class="topbar">
  <div class="account"><a href="#">Sign up</a><a href="#">Log in</a></div>
</div>

<header class="header">
  <div class="brand"><span class="dot"></span><span class="name">fund in Kenya</span></div>
  <nav class="nav">
    <a class="active" href="#">Home</a>
    <a href="#">About Ghana</a>
    <a href="#">Why Ghana</a>
    <a href="#">Sponsorship</a>
    <a href="#">News &amp; Media</a>
    <a href="#">Contact us</a>
  </nav>
</header>

<section class="hero" role="img" aria-label="Photograph of a modern city skyline with office towers and a road">
  <div class="caption"><h1>Ghana has become something of a leading light in the continent of Africa</h1></div>
  <div class="pager"><span></span><span class="on"></span><span></span><span></span></div>
</section>

<section class="wrap featured">
  <div class="label">As featured in</div>
  <div class="logos">
    <div class="badge" style="width:150px"></div>
    <div class="badge" style="width:170px"></div>
    <div class="badge" style="width:110px"></div>
    <div class="badge" style="width:130px"></div>
    <div class="badge" style="width:140px;background:#e0e0e0"></div>
  </div>
</section>

<section class="wrap intro">
  <div class="col">
    <h2 class="heading">About Ghana</h2>
    <p>On the 6th of March 1957, formerly known as the Gold Coast, Ghana became independent from British colonial rule. It became the first African colony to gain independence.</p>
    <p>Ghana is rich in minerals such as gold, diamonds, manganese, limestone, bauxite, iron ore as well as various granite deposits and clay. Ghana is estimated to have a population of over 25 million and this figure grows 2.5% annually. The majority of the population are based in the southern side of Ghana which has the highest density occurring in urban and cocoa producing areas.</p>
    <a class="btn" href="#">Read more</a>
  </div>
  <div class="col">
    <h2 class="heading">Why Ghana</h2>
    <div class="why-body">
      <div class="why-media" role="img" aria-label="Photograph of hands reviewing financial charts and graphs on paper"></div>
      <div class="why-text">
        <p>On the 6th of March 1957 formerly known as the Gold Coast, Ghana became independent from British colonial rule.</p>
        <h3>Strengths of the market</h3>
        <ul>
          <li>A judicial system based on English law and the Rule of Law is increasingly being improved.</li>
          <li>A growing trading hub for West Africa with a deep sea port at Tema servicing the region.</li>
        </ul>
      </div>
    </div>
    <a class="btn" href="#">Read more</a>
  </div>
</section>

<h2 class="wrap heading popular-title">What's popular</h2>
<section class="popular">
  <div class="cards">
    <article class="card">
      <div class="media m-port" role="img" aria-label="Photograph of a container ship at a port"></div>
      <h4>Steady Economic Growth</h4>
      <p>Ghana has enjoyed steady growth over the past decade with between 4-7 and 7.2 GDP growths, GDP growth for 2011 was.</p>
      <div class="place"><svg width="10" height="13" viewBox="0 0 10 13"><path d="M5 0a5 5 0 0 0-5 5c0 3.5 5 8 5 8s5-4.5 5-8a5 5 0 0 0-5-5zm0 7a2 2 0 1 1 0-4 2 2 0 0 1 0 4z" fill="#8a8a8a"/></svg>Washington, DC</div>
      <div class="bar"><span></span></div>
      <div class="stats"><div><b>100%</b><small>funded</small></div><div><b>$1,351,963</b><small>pledged</small></div><div><b>7</b><small>days to go</small></div></div>
    </article>
    <article class="card">
      <div class="media m-road" role="img" aria-label="Photograph of a cargo truck on a highway"></div>
      <h4>Steady Economic Growth</h4>
      <p>Ghana has enjoyed steady growth over the past decade with between 4-7 and 7.2 GDP growths, GDP growth for 2011 was.</p>
      <div class="place"><svg width="10" height="13" viewBox="0 0 10 13"><path d="M5 0a5 5 0 0 0-5 5c0 3.5 5 8 5 8s5-4.5 5-8a5 5 0 0 0-5-5zm0 7a2 2 0 1 1 0-4 2 2 0 0 1 0 4z" fill="#8a8a8a"/></svg>Washington, DC</div>
      <div class="bar"><span></span></div>
      <div class="stats"><div><b>100%</b><small>funded</small></div><div><b>$1,351,963</b><small>pledged</small></div><div><b>7</b><small>days to go</small></div></div>
    </article>
    <article class="card">
      <div class="media m-pipe" role="img" aria-label="Photograph of yellow industrial gas pipelines"></div>
      <h4>Steady Economic Growth</h4>
      <p>Ghana has enjoyed steady growth over the past decade with between 4-7 and 7.2 GDP growths, GDP growth for 2011 was.</p>
      <div class="place"><svg width="10" height="13" viewBox="0 0 10 13"><path d="M5 0a5 5 0 0 0-5 5c0 3.5 5 8 5 8s5-4.5 5-8a5 5 0 0 0-5-5zm0 7a2 2 0 1 1 0-4 2 2 0 0 1 0 4z" fill="#8a8a8a"/></svg>Washington, DC</div>
      <div class="bar"><span></span></div>
      <div class="stats"><div><b>100%</b><small>funded</small></div><div><b>$1,351,963</b><small>pledged</small></div><div><b>7</b><small>days to go</small></div></div>
    </article>
  </div>
</section>

<h2 class="wrap heading news-title">News &amp; Media</h2>
<section class="wrap news">
  <article class="item">
    <div class="thumb t1" role="img" aria-label="News photograph of a press event"></div>
    <div><h5>RDA's Revenge on the People of Ghana - Kestrel News</h5><time>July 6, 2015</time><p>Ghana has enjoyed steady growth over the past decade with between 4-7 and 7.2 GDP growths.</p></div>
  </article>
  <article class="item">
    <div class="thumb t2" role="img" aria-label="News photograph of a public gathering"></div>
    <div><h5>RDA's Revenge on the People of Ghana - Kestrel News</h5><time>July 6, 2015</time><p>Ghana has enjoyed steady growth over the past decade with between 4-7 and 7.2 GDP growths.</p></div>
  </article>
  <article class="item">
    <div class="thumb t3" role="img" aria-label="News photograph of a market street"></div>
    <div><h5>RDA's Revenge on the People of Ghana - Kestrel News</h5><time>July 6, 2015</time><p>Ghana has enjoyed steady growth over the past decade with between 4-7 and 7.2 GDP growths.</p></div>
  </article>
  <article class="item">
    <div class="thumb t4" role="img" aria-label="News photograph of farmland"></div>
    <div><h5>RDA's Revenge on the People of Ghana - Kestrel News</h5><time>July 6, 2015</time><p>Ghana has enjoyed steady growth over the past decade with between 4-7 and 7.2 GDP growths.</p></div>
  </article>
</section>

<footer class="footer">
  <nav class="links">
    <a href="#">Home</a><a href="#">About Ghana</a><a href="#">Why Ghana</a><a href="#">Sponsorship</a><a href="#">News &amp; Media</a><a href="#">Contact us</a>
  </nav>
  <div class="social"><span></span><span></span><span></span><span></span></div>
  <div class="base"><p>Copyright 2015 fund in Kenya. All Rights Reserved.</p></div>
</footer>

</body>
</html>
```